HARD MONEY ORIGINATOR RECRUITMENT.
Looking for individuals to help us originate loans for real estate investor financing primarily used to fix up properties and resell.
HARD MONEY ORIGINATORS WANTED
No Licensing Required
Work As Independent Contractor
1% Flat Finders Fee on Each Loan
Referral Compensation for Recruiting New Originators
Immediate Payouts
Programs Offered Nationwide
Marketing Assistance and Support Available
Email mpelton@brightquaylending.com for more information or call (800) 641-2950 Ext. 24 Brightquay Lending Services, Inc. www.brightquaylending.com NMLS #318760
Industry/Entity Type
Real Estate
Look and feel
Each slider illustrates characteristics of the customer's brand and the style your logo design should communicate.

```html
<!DOCTYPE html>
<html lang="en">
<head>
<meta charset="utf-8">
<title>Hard Money Originators Wanted – Brightquay Lending Services, Inc.</title>
<link rel="stylesheet" href="https://fonts.googleapis.com/css2?family=Libre+Franklin:wght@300;400;600;700;900&display=swap">
<style>
  :root {
    --navy: #0f4a86;
    --navy-deep: #0b3d73;
    --gold: #b3a23a;
    --gold-light: #d8cf8a;
    --tick: #5fb53a;
    --white: #ffffff;
    --ink-blue: #1b5aa3;
    --stage: #e9e9e9;
  }
  * { margin: 0; padding: 0; box-sizing: border-box; }
  html, body {
    width: 1200px; height: 1000px; overflow: hidden;
    background: radial-gradient(ellipse at center, #f7f7f7 0%, var(--stage) 70%, #d4d4d4 100%);
    font-family: "Libre Franklin", Arial, sans-serif;
  }
  .postcard {
    position: absolute; left: 120px; top: 200px;
    width: 960px; height: 600px;
    background: var(--white);
    box-shadow: 0 14px 40px rgba(0,0,0,.28);
    overflow: hidden;
  }
  .postcard-shapes { position: absolute; inset: 0; width: 960px; height: 600px; }
  .hero-photo {
    position: absolute; left: 0; top: 0; width: 450px; height: 244px;
    background: linear-gradient(160deg, #eef0ec 0%, #dcdcd6 40%, #c9a27a 78%, #a57a4f 100%);
  }
  .brand-block {
    position: absolute; left: 470px; top: 0; width: 490px; height: 230px;
    display: flex; align-items: center; justify-content: center; gap: 14px;
  }
  .brand-dot { width: 26px; height: 26px; border-radius: 50%; background: var(--gold); flex: none; }
  .brand-name { font-weight: 700; font-size: 27px; color: var(--ink-blue); letter-spacing: .2px; }
  .headline { position: absolute; left: 44px; top: 262px; color: var(--white); }
  .headline-top { font-weight: 900; font-size: 37px; line-height: 1; letter-spacing: .5px; }
  .headline-mid { font-weight: 300; font-size: 45px; line-height: 1.05; letter-spacing: 1px; margin-top: 2px; }
  .headline-main { font-weight: 900; font-size: 88px; line-height: .95; letter-spacing: 1px; }
  .site-url { font-weight: 600; font-size: 25px; color: var(--gold-light); margin-top: 8px; letter-spacing: .3px; }
  .benefits { position: absolute; left: 515px; top: 254px; list-style: none; color: var(--white); }
  .benefits li {
    display: flex; align-items: flex-start; gap: 9px;
    font-weight: 600; font-size: 15px; line-height: 1.2; margin-bottom: 10px;
  }
  .benefits svg { flex: none; width: 18px; height: 16px; margin-top: -1px; }
  .contact-line {
    position: absolute; left: 0; width: 960px; top: 508px; text-align: center;
    color: var(--white); font-size: 18px; font-weight: 400;
  }
  .contact-line b { font-weight: 700; }
  .contact-line .phone { font-weight: 700; font-size: 21px; }
  .legal-line {
    position: absolute; left: 0; width: 960px; top: 564px; text-align: center;
    color: var(--white); font-size: 15px; font-weight: 400; letter-spacing: .2px;
  }
</style>
</head>
<body>
  <article class="postcard">
    <div class="hero-photo" role="img" aria-label="Photo of two professionals reviewing plans in a renovated kitchen, with line-drawn ladder, plant and light fixtures"></div>

    <div class="brand-block">
      <span class="brand-dot"></span>
      <span class="brand-name">Brightquay Lending Services, Inc.</span>
    </div>

    <svg class="postcard-shapes" viewBox="0 0 960 600" aria-hidden="true">
      <path d="M0 238 L600 238 C760 238 860 214 960 200" fill="none" stroke="var(--gold)" stroke-width="5"/>
      <path d="M0 245 L600 245 C760 245 860 222 960 208 L960 600 L0 600 Z" fill="var(--navy)"/>
      <path d="M0 500 L650 500 C790 500 880 478 960 462 L960 518 C880 530 790 548 650 550 L0 550 Z" fill="var(--gold)"/>
      <path d="M0 550 L650 550 C790 548 880 530 960 518 L960 600 L0 600 Z" fill="var(--navy-deep)"/>
    </svg>

    <div class="headline">
      <div class="headline-top">HARD MONEY</div>
      <div class="headline-mid">ORIGINATORS</div>
      <div class="headline-main">WANTED</div>
      <div class="site-url">www.brightquaylending.com</div>
    </div>

    <ul class="benefits">
      <li><svg viewBox="0 0 18 16"><path d="M1 9 L6 14 L17 2" fill="none" stroke="var(--tick)" stroke-width="3.2" stroke-linecap="round" stroke-linejoin="round"/></svg>No Licensing Required</li>
      <li><svg viewBox="0 0 18 16"><path d="M1 9 L6 14 L17 2" fill="none" stroke="var(--tick)" stroke-width="3.2" stroke-linecap="round" stroke-linejoin="round"/></svg>Work As Independent Contractor</li>
      <li><svg viewBox="0 0 18 16"><path d="M1 9 L6 14 L17 2" fill="none" stroke="var(--tick)" stroke-width="3.2" stroke-linecap="round" stroke-linejoin="round"/></svg>1% Flat Finders Fee on Each Loan</li>
      <li><svg viewBox="0 0 18 16"><path d="M1 9 L6 14 L17 2" fill="none" stroke="var(--tick)" stroke-width="3.2" stroke-linecap="round" stroke-linejoin="round"/></svg><span>Referral Compensation for Recruiting<br>New Originators</span></li>
      <li><svg viewBox="0 0 18 16"><path d="M1 9 L6 14 L17 2" fill="none" stroke="var(--tick)" stroke-width="3.2" stroke-linecap="round" stroke-linejoin="round"/></svg>Immediate Payouts</li>
      <li><svg viewBox="0 0 18 16"><path d="M1 9 L6 14 L17 2" fill="none" stroke="var(--tick)" stroke-width="3.2" stroke-linecap="round" stroke-linejoin="round"/></svg>Programs Offered Nationwide</li>
      <li><svg viewBox="0 0 18 16"><path d="M1 9 L6 14 L17 2" fill="none" stroke="var(--tick)" stroke-width="3.2" stroke-linecap="round" stroke-linejoin="round"/></svg>Marketing Assistance and Support Available</li>
    </ul>

    <p class="contact-line"><b>Email</b> mpelton@brightquaylending.com for more information or <span class="phone">Call (800) 641-2950</span></p>
    <p class="legal-line">Ext. 24 Brightquay Lending Services, Inc.&nbsp; NMLS #318760</p>
  </article>
</body>
</html>
```